Redesign Current Website Into An Exciting Updated Design

We need to redesign the current website www.glintvaultoffers.net We want an overall new look. We are rebranding so it will be a new logo and we would like to see new images as well so you cannot compare the old from the new.

You can use same exact content as on current url www.glintvaultoffers.net

The website must be warm and inviting and fun yet professional and modern.

The website must also be designed with mobile in mind

The website must be warm and inviting yet professional and modern.

The website must also be designed with mobile in mind.

Target Market(s)

Consumers redeeming rewards

Industry/Entity Type

Promotional Reward Fullfillment

Coding

Coded - Design and coding required

Number of Pages Required

3 page

Requirements
Must have
• This website is a website where consumers come to redeem rewards they received from doing business with a company that offers these rewards. So the website should be very inviting.
Nice to have
• open
Should not have
• open

```html
<!DOCTYPE html>
<html lang="en">
<head>
<meta charset="utf-8">
<title>Kindly Rewards – Online Redemption System</title>
<link href="https://fonts.googleapis.com/css2?family=Montserrat:wght@600;700;800&family=Mulish:wght@400;600;700&display=swap" rel="stylesheet">
<style>
:root{
  --blue:#276494;
  --blue-dark:#1f5584;
  --ink:#2f2f33;
  --muted:#555a60;
  --hero-bg:#f5f3f4;
  --about-bg:#eef5fb;
  --lavender:#d6d6f3;
  --white:#ffffff;
}
*{box-sizing:border-box;margin:0;padding:0}
html,body{width:1200px;height:2998px;overflow:hidden}
body{font-family:'Mulish',sans-serif;color:var(--ink);background:var(--white)}
.page{position:relative;width:1200px;height:2998px;overflow:hidden;background:var(--white)}
.abs{position:absolute}

/* header / hero */
.hero{position:absolute;left:0;top:0;width:1200px;height:689px;background:var(--hero-bg)}
.brand{position:absolute;left:151px;top:40px;font-family:'Montserrat',sans-serif;font-weight:800;font-size:26px;line-height:28px;color:var(--blue);letter-spacing:.5px}
.nav{position:absolute;top:36px;left:574px;display:flex;align-items:center;height:30px}
.nav a{font-family:'Montserrat',sans-serif;font-weight:700;font-size:13px;color:var(--blue);text-decoration:none;position:absolute;white-space:nowrap;top:7px}
.nav .active{left:0;top:0;width:74px;height:30px;border-radius:15px;background:var(--blue);color:var(--white);text-align:center;line-height:30px}
.hero-photo{position:absolute;left:155px;top:175px;width:435px;height:514px;border-radius:200px 200px 0 0;background:linear-gradient(180deg,var(--lavender) 0%,#a9b3cc 55%,#5c7593 100%)}
.bubble{position:absolute;left:143px;top:544px;width:227px;height:137px;background:var(--blue);border-radius:70px 110px 40px 70px;color:var(--white);font-family:'Montserrat',sans-serif;font-weight:700;font-size:17px;line-height:21px;text-align:center;padding-top:28px;padding-right:30px}
.bubble svg{display:block;margin:0 auto 6px}
.hero-title{position:absolute;left:664px;top:128px;font-family:'Montserrat',sans-serif;font-weight:800;font-size:54px;line-height:56px;color:var(--blue)}
.hero-text{position:absolute;left:669px;top:316px;width:385px;font-size:14.5px;line-height:21px;color:var(--ink)}
.field{position:absolute;left:667px;width:381px;height:48px;border-radius:24px;background:var(--white);box-shadow:0 2px 8px rgba(0,0,0,.06);font-size:14px;color:var(--muted);line-height:48px;padding-left:28px}
.go{position:absolute;left:668px;top:573px;width:382px;height:49px;border-radius:25px;background:var(--blue);color:var(--white);font-family:'Montserrat',sans-serif;font-weight:800;font-size:22px;display:flex;align-items:center;justify-content:center;gap:18px}

/* partner strip */
.partners{position:absolute;left:0;top:689px;width:1200px;height:118px;background:var(--white);box-shadow:0 3px 6px rgba(0,0,0,.08)}
.partner{position:absolute;top:43px;font-family:'Montserrat',sans-serif;font-weight:700;font-size:22px;color:var(--ink);text-align:center;width:140px}
.arrow{position:absolute;top:42px}

/* categories */
.cat{position:absolute;overflow:hidden}
.cat span{position:absolute;font-family:'Montserrat',sans-serif;font-weight:700;font-size:14px;line-height:18px;color:var(--white)}

/* about */
.about{position:absolute;left:0;top:1370px;width:1200px;height:627px;background:var(--about-bg)}
.about-frame{position:absolute;left:157px;top:1450px;width:150px;height:98px;border-left:2px solid var(--blue);border-top:2px solid var(--blue);border-bottom:2px solid var(--blue);border-right:none}
.about-title{position:absolute;left:182px;top:1480px;font-family:'Montserrat',sans-serif;font-weight:800;font-size:36px;color:var(--blue);background:var(--about-bg);padding-right:8px}
.about-text{position:absolute;left:157px;top:1576px;width:431px;font-size:13px;line-height:18px;text-align:justify;color:var(--ink)}
.about-text p+p{margin-top:18px}
.btn-more{position:absolute;left:157px;top:1907px;width:120px;height:38px;border-radius:19px;background:var(--blue);color:var(--white);font-family:'Montserrat',sans-serif;font-weight:700;font-size:12px;text-align:center;line-height:38px}
.about-photo{position:absolute;left:646px;top:1423px;width:402px;height:520px;border-radius:22px;background:radial-gradient(circle at 50% 70%,#e0493d 0 10%,transparent 11%),linear-gradient(180deg,#e9dccb 0%,#f1ebe2 40%,#d9c2ad 100%)}

/* testimonials */
.section-title{position:absolute;left:0;width:1200px;text-align:center;top:2045px;font-family:'Montserrat',sans-serif;font-weight:800;font-size:37px;color:var(--blue)}
.rule{position:absolute;left:576px;top:2121px;width:47px;height:3px;background:var(--blue)}
.t-card{position:absolute;left:150px;top:2177px;width:900px;height:384px;border-radius:20px;background:var(--white);box-shadow:0 4px 20px rgba(0,0,0,.05)}
.t-photo{position:absolute;left:204px;top:2206px;width:326px;height:326px;border-radius:50%;background:radial-gradient(circle,#e7a64e 0%,#7fa6d6 55%,rgba(255,255,255,0) 72%)}
.quote-mark{position:absolute;left:590px;top:2205px;font-family:'Montserrat',sans-serif;font-weight:800;font-size:80px;color:var(--blue);line-height:80px}
.t-text{position:absolute;left:648px;top:2250px;width:370px;font-size:23px;line-height:33px;color:var(--ink)}
.t-rule{position:absolute;left:648px;top:2473px;width:40px;height:2px;background:var(--blue)}
.t-name{position:absolute;left:648px;top:2491px;font-weight:700;font-size:18px;color:var(--blue)}
.dot{position:absolute;top:2609px;width:13px;height:13px;border-radius:50%;border:1.5px solid var(--blue)}
.dot.on{background:var(--blue)}

/* footer */
.footer-wave{position:absolute;left:0;top:2660px}
.footer-brand{position:absolute;left:0;width:1200px;top:2800px;text-align:center;font-family:'Montserrat',sans-serif;font-weight:800;font-size:34px;line-height:40px;color:var(--white)}
.footer-links{position:absolute;left:0;width:1200px;top:2938px;text-align:center;font-size:14px;color:var(--white)}
</style>
</head>
<body>
<div class="page">

  <section class="hero">
    <div class="brand">KINDLY<br>REWARDS</div>
    <nav class="nav">
      <a class="active" href="#">HOME</a>
      <a href="#" style="left:96px">TESTIMONIALS</a>
      <a href="#" style="left:242px">ALREADY REDEEMED?</a>
      <a href="#" style="left:435px">HELP</a>
    </nav>
    <div class="hero-photo" role="img" aria-label="Smiling man holding out a wrapped gift box with a red ribbon"></div>
    <div class="bubble">
      <svg width="24" height="22" viewBox="0 0 24 22" fill="none" stroke="#fff" stroke-width="2"><rect x="2" y="8" width="20" height="5" fill="#fff"/><rect x="4" y="13" width="16" height="8" fill="#fff"/><path d="M12 8c-2-5-7-5-6-1M12 8c2-5 7-5 6-1"/></svg>
      Redeem Your<br>Offer Now
    </div>
    <h1 class="hero-title">ONLINE<br>REDEMPTION<br>SYSTEM</h1>
    <p class="hero-text">To Learn More About Your Offer Including The Full Details, How It Works, Terms, FAQ's and To Redeem and Activate Your Certificate Please Enter A Valid Certificate Number and Email.</p>
    <div class="field" style="top:431px">Certificate ID</div>
    <div class="field" style="top:498px">Email Address</div>
    <div class="go">GO
      <svg width="38" height="16" viewBox="0 0 38 16" fill="none" stroke="#fff" stroke-width="2.2"><path d="M1 8h34M28 1l7 7-7 7"/></svg>
    </div>
  </section>

  <section class="partners">
    <svg class="arrow" style="left:92px" width="16" height="30" viewBox="0 0 16 30" fill="none" stroke="#276494" stroke-width="2"><path d="M14 2L2 15l12 13"/></svg>
    <div class="partner" style="left:139px">Northwind</div>
    <div class="partner" style="left:299px">Baylark</div>
    <div class="partner" style="left:464px;font-size:17px;line-height:19px;top:34px">Coldmere<br>Homes</div>
    <div class="partner" style="left:636px">DirectHaul</div>
    <div class="partner" style="left:796px">Haveno</div>
    <div class="partner" style="left:940px">Beamline</div>
    <svg class="arrow" style="left:1095px" width="16" height="30" viewBox="0 0 16 30" fill="none" stroke="#276494" stroke-width="2"><path d="M2 2l12 13L2 28"/></svg>
  </section>

  <section class="categories">
    <div class="cat" style="left:149px;top:875px;width:343px;height:424px;border-radius:172px 172px 0 0;background:linear-gradient(180deg,#dfe5ea 0%,#b8ccdc 45%,#6f8fb0 100%)" role="img" aria-label="Family running on a beach with a kite">
      <span style="left:18px;bottom:20px">VACATION<br>CERTIFICATES</span>
    </div>
    <div class="cat" style="left:513px;top:869px;width:260px;height:207px;border-radius:130px 130px 0 0;background:linear-gradient(180deg,#e5bfae 0%,#8aa2bf 45%,#2f5d8a 100%)" role="img" aria-label="Hiker on a mountain summit">
      <span style="left:19px;bottom:14px">TRAVEL<br>VOUCHERS</span>
    </div>
    <div class="cat" style="left:790px;top:869px;width:260px;height:207px;border-radius:130px 130px 0 0;background:linear-gradient(180deg,#c7b7a4 0%,#9aa6b3 50%,#38628c 100%)" role="img" aria-label="Dinner table with plates and a glass of champagne">
      <span style="left:19px;bottom:14px">DINING<br>INCENTIVES</span>
    </div>
    <div class="cat" style="left:513px;top:1094px;width:260px;height:205px;border-radius:0 0 110px 0;background:linear-gradient(180deg,#6e8f6b 0%,#7a9ab3 50%,#2f5d8a 100%)" role="img" aria-label="Hands holding a smartphone">
      <span style="left:19px;bottom:12px">DIGITAL<br>ELECTRONIC<br>PRODUCTS</span>
    </div>
    <div class="cat" style="left:790px;top:1094px;width:260px;height:205px;border-radius:0 0 0 110px;background:linear-gradient(180deg,#b9876d 0%,#7c93ae 50%,#2f5d8a 100%)" role="img" aria-label="Convenience store shelves with groceries">
      <span style="left:75px;bottom:28px">GAS &amp; GROCERY<br>REWARDS</span>
    </div>
  </section>

  <section class="about"></section>
  <div class="about-frame"></div>
  <h2 class="about-title">ABOUT US</h2>
  <div class="about-text">
    <p>We provide marketing incentives in the form of gift certificates and vouchers that are redeemable for a variety of items such as: discount travel, smart device products, restaurant incentives , golf discounts and more to thousands of businesses around the world who use them to create exciting marketing promotions and giveaways, customer loyalty programs, promotional contests and use them as customer appreciation gifts.</p>
    <p>We are simply a 3rd party administrator that handles the redemption and fulfillment processing for a variety of incentive gifts and rewards. We have created the platform that facilitates the redemption and fulfillment process in a comprehensive, an easy to use online interface. Simply enter your code and email to redeem your offer and follow the steps to complete the fulfillment process to receive your gift. We work with thousands of large corporations and even small independently owned businesses that trust us to take care of their customers. It's our goal to make it easy for you to redeem your offer.</p>
  </div>
  <div class="btn-more">READ MORE</div>
  <div class="about-photo" role="img" aria-label="Woman holding a small red gift box with a teal bow"></div>

  <h2 class="section-title">TESTIMONIALS</h2>
  <div class="rule"></div>
  <div class="t-card"></div>
  <div class="t-photo" role="img" aria-label="Happy traveller in a straw hat and sunglasses"></div>
  <div class="quote-mark">&ldquo;</div>
  <p class="t-text">The trip to Vegas was the perfect getaway for my husband and I. The city that never stops. It has a little of everything from sight seeing to fun all-night options. We had a blast!!!</p>
  <div class="t-rule"></div>
  <div class="t-name">Marisol T.</div>
  <span class="dot on" style="left:567px"></span>
  <span class="dot" style="left:594px"></span>
  <span class="dot" style="left:620px"></span>

  <svg class="footer-wave" width="1200" height="338" viewBox="0 0 1200 338">
    <path d="M0 20 C300 90 700 -10 1200 30 L1200 338 L0 338Z" fill="#e7e9ec"/>
    <path d="M0 50 C300 120 750 20 1200 45 L1200 338 L0 338Z" fill="#276494"/>
  </svg>
  <div class="footer-brand">KINDLY<br>REWARDS</div>
  <div class="footer-links">Privacy Policy &nbsp;&nbsp;|&nbsp;&nbsp; Terms Of Use &nbsp;&nbsp;|&nbsp;&nbsp; © Copyright 2005-2025. All Rights Reserved.</div>

</div>
</body>
</html>
```